WordPress Website for Pain Relief Clinic

I need a WordPress website designed for my laser pain relief clinic. It needs to be a professional, responsive design with 7 pages: Home, Why Choose Us, Treatable Conditions, Testimonials, FAQ, Franchising, Contact Us. Here is logo: https://files.brivoltcdn.com/media.t-w-e-n.com/sitebuilder/472/CalvexaLogoHighQuality.png

Target Market(s)

people with pain,elderly adults,injuries,soreness

Industry/Entity Type

Clinic

Number of Pages Required

5+ page

Colors
0792cd
85abd2

```html
<!DOCTYPE html>
<html lang="en">
<head>
<meta charset="utf-8">
<title>Calvexa Pain Treatment Center</title>
<link rel="stylesheet" href="https://fonts.googleapis.com/css2?family=Open+Sans:wdth,wght@75..100,300..800&display=swap">
<style>
:root{
  --blue:#0792cd;
  --blue-dark:#1565b4;
  --blue-soft:#85abd2;
  --red:#b5171b;
  --page:#eef4fb;
  --white:#ffffff;
  --text:#555a60;
  --ink:#222;
  --line:#e3e8ee;
}
*{box-sizing:border-box;margin:0;padding:0}
html,body{width:1155px;height:1200px;overflow:hidden}
body{background:var(--page);font-family:"Open Sans",sans-serif;color:var(--text);position:relative}
.cond{font-stretch:75%}
a{color:var(--blue-dark)}
.site-header{position:absolute;left:0;top:0;width:1155px;height:43px;background:var(--page);border-bottom:1px solid #c9d3dd}
.brand{position:absolute;left:218px;top:6px;display:flex;align-items:center;gap:6px;font-family:"Open Sans",sans-serif;font-weight:800;font-size:24px;color:var(--blue-dark);letter-spacing:-.5px}
.brand-mark{width:12px;height:12px;background:var(--red);border-radius:50%}
.main-nav{position:absolute;left:458px;top:0;display:flex;height:43px}
.main-nav a{font-stretch:75%;font-weight:500;font-size:13px;color:#333;text-decoration:none;padding:0 10px;line-height:43px;text-transform:uppercase}
.main-nav a.active{background:var(--red);color:#fff}
.hero{position:absolute;left:0;top:43px;width:1155px;height:381px;background:linear-gradient(90deg,#1e4a7c 0%,#2c6aa6 35%,#5f88ad 55%,#c59b8c 68%,#9fb0c4 82%,#2b5b8e 100%)}
.hero-text{position:absolute;left:219px;top:153px;color:#fff;font-stretch:75%}
.hero-text .welcome{font-size:28px;font-weight:400;line-height:34px}
.hero-text h1{font-size:35px;font-weight:800;line-height:36px}
.quick-links{position:absolute;left:218px;top:439px;width:732px;height:92px;background:#fff;display:flex;box-shadow:0 1px 2px rgba(0,0,0,.1)}
.quick-card{flex:1;display:flex;align-items:flex-start;padding:23px 20px 0 22px;border-right:1px solid var(--line)}
.quick-card:last-child{border-right:0}
.quick-card svg{flex:none;margin-right:10px}
.quick-card h3{font-stretch:75%;font-weight:700;font-size:17px;color:var(--blue-dark);line-height:20px}
.quick-card p{font-size:10px;line-height:14px;color:#333}
.facilities{position:absolute;left:218px;top:548px;width:161px;background:#fff;box-shadow:0 1px 2px rgba(0,0,0,.1)}
.facilities h2{background:var(--blue-dark);color:#fff;font-stretch:75%;font-weight:700;font-size:17px;height:32px;line-height:32px;padding-left:7px}
.facilities li{list-style:none;display:flex;justify-content:space-between;align-items:center;font-size:10px;color:#333;padding:4px 8px 4px 6px;min-height:26px;line-height:14px}
.facilities li:nth-child(even){background:#f3f6f9}
.about{position:absolute;left:393px;top:548px;width:557px;height:364px;background:#fff;box-shadow:0 1px 2px rgba(0,0,0,.1)}
.about h2{background:var(--red);color:#fff;font-stretch:75%;font-weight:700;font-size:17px;height:32px;line-height:32px;padding-left:7px}
.about p{font-size:10.3px;line-height:17.2px;color:var(--text);position:absolute}
.about .intro{left:18px;top:45px;width:270px}
.about .more{left:18px;top:252px;width:522px}
.about-photo{position:absolute;left:302px;top:53px;width:240px;height:159px;background:linear-gradient(135deg,#b8a89c 0%,#d9b79c 40%,#c99a7f 70%,#eee 100%)}
.site-footer{position:absolute;left:0;top:930px;width:1155px;height:214px;background:var(--blue);color:#fff}
.footer-col{position:absolute;top:27px}
.footer-col h4{font-size:13px;font-weight:600;color:#1b1b1b;margin-bottom:5px}
.footer-col li{list-style:none;font-size:10.5px;line-height:17.2px}
.social li{display:flex;align-items:center;gap:10px;height:32px;line-height:32px}
.social .icon{width:21px;height:21px;background:#fff;border-radius:2px}
.copyright{position:absolute;left:0;top:1144px;width:1155px;height:56px;background:var(--red);color:#fff;font-size:10.5px;padding:22px 0 0 214px}
</style>
</head>
<body>
<header class="site-header">
  <div class="brand"><span>Calvexa</span><span class="brand-mark"></span></div>
  <nav class="main-nav">
    <a class="active" href="#">Home</a><a href="#">Why Choose Us</a><a href="#">Treatable Conditions</a><a href="#">Testimonials</a><a href="#">FAQ</a><a href="#">Franchising</a><a href="#">Contact Us</a>
  </nav>
</header>

<section class="hero" role="img" aria-label="Woman holding her sore shoulder in a blue clinic setting">
  <div class="hero-text">
    <div class="welcome">WELCOME TO</div>
    <h1>CALVEXA PAIN<br>TREATMENT CENTER</h1>
  </div>
</section>

<section class="quick-links">
  <div class="quick-card">
    <svg width="46" height="46" viewBox="0 0 46 46"><circle cx="23" cy="23" r="23" fill="#d8312b"/><rect x="14" y="12" width="18" height="23" rx="3" fill="#fff"/><rect x="19" y="9" width="8" height="5" rx="2" fill="#fff"/><rect x="17" y="20" width="12" height="2" fill="#d8312b"/><rect x="17" y="25" width="8" height="2" fill="#d8312b"/></svg>
    <div><h3>CarePortal Access</h3><p><a href="#">Sign in</a> to your CarePortal or <a href="#">request access</a> to get started.</p></div>
  </div>
  <div class="quick-card">
    <svg width="46" height="46" viewBox="0 0 46 46"><circle cx="23" cy="23" r="23" fill="#2a86d0"/><rect x="11" y="16" width="24" height="17" rx="3" fill="#fff"/><rect x="26" y="22" width="9" height="6" rx="2" fill="#2a86d0"/><circle cx="29" cy="25" r="1.5" fill="#fff"/></svg>
    <div><h3>Health Cost Estimator</h3><p>Find out the <a href="#">cost of health care services</a>.</p></div>
  </div>
  <div class="quick-card">
    <svg width="46" height="46" viewBox="0 0 46 46"><circle cx="23" cy="23" r="23" fill="#a57c67"/><circle cx="23" cy="16" r="6" fill="#fff"/><path d="M12 36c0-8 5-12 11-12s11 4 11 12z" fill="#fff"/></svg>
    <div><h3>Find a Physician</h3><p>Looking for a specialist? <a href="#">Start here</a>.</p></div>
  </div>
</section>

<aside class="facilities">
  <h2 class="cond">Patient Care Facilities</h2>
  <ul>
    <li>Brightwater Memorial Hospital<svg width="7" height="11" viewBox="0 0 7 11"><path d="M1 1l4.5 4.5L1 10" stroke="#1565b4" stroke-width="1.6" fill="none"/></svg></li>
    <li>Maplecrest Children's Hospital<svg width="7" height="11" viewBox="0 0 7 11"><path d="M1 1l4.5 4.5L1 10" stroke="#1565b4" stroke-width="1.6" fill="none"/></svg></li>
    <li>Ridgeview Hospital<svg width="7" height="11" viewBox="0 0 7 11"><path d="M1 1l4.5 4.5L1 10" stroke="#1565b4" stroke-width="1.6" fill="none"/></svg></li>
    <li>Larkfield Health<svg width="7" height="11" viewBox="0 0 7 11"><path d="M1 1l4.5 4.5L1 10" stroke="#1565b4" stroke-width="1.6" fill="none"/></svg></li>
    <li>Ashdown Cancer Institute<svg width="7" height="11" viewBox="0 0 7 11"><path d="M1 1l4.5 4.5L1 10" stroke="#1565b4" stroke-width="1.6" fill="none"/></svg></li>
    <li>Corwin Eye Institute<svg width="7" height="11" viewBox="0 0 7 11"><path d="M1 1l4.5 4.5L1 10" stroke="#1565b4" stroke-width="1.6" fill="none"/></svg></li>
    <li>Halbrook Institute for Oral Health<svg width="7" height="11" viewBox="0 0 7 11"><path d="M1 1l4.5 4.5L1 10" stroke="#1565b4" stroke-width="1.6" fill="none"/></svg></li>
    <li>View more facilities<svg width="7" height="11" viewBox="0 0 7 11"><path d="M1 1l4.5 4.5L1 10" stroke="#1565b4" stroke-width="1.6" fill="none"/></svg></li>
  </ul>
</aside>

<section class="about">
  <h2 class="cond">About Calvexa Company</h2>
  <p class="intro">Lorem ipsum dolor sit ipsum Lorem ipsum dolor sit ipsum Lorem ipsum dolor sit ipsum Lorem ipsum dolor sit ipsum Lorem ipsum dolor sit ipsum Lorem ipsum dolor sit ipsum Lorem ipsum dolor sit ipsum Lorem ipsum dolor sit ipsumLorem ipsum dolor sit ipsum Lorem ipsum dolor sit ipsum Lorem ipsum dolor sit ipsum Lorem ipsum dolor sit ipsum Lorem ipsum dolor sit ipsum Lorem ipsum dolor sit ipsum Lorem ipsum dolor sit ipsum Lorem ipsum dolor sit ipsum Lorem ipsum dolor sit ipsum Lorem ipsum dolor sit</p>
  <div class="about-photo" role="img" aria-label="Therapist's hands massaging a patient's shoulder"></div>
  <p class="more">Lorem ipsum dolor sit ipsum Lorem ipsum dolor sit ipsum Lorem ipsum dolor sit ipsum Lorem ipsum dolor sit ipsum Lorem ipsum dolor sit ipsum Lorem ipsum dolor sit ipsum Lorem ipsum dolor sit ipsum Lorem ipsum dolor sit ipsumLorem ipsum dolor sit ipsum Lorem ipsum dolor sit ipsum Lorem ipsum dolor sit ipsum Lorem ipsum dolor sit ipsum Lorem ipsum dolor sit ipsum Lorem ipsum dolor sit ipsum Lorem ipsum dolor sit</p>
</section>

<footer class="site-footer">
  <div class="footer-col" style="left:216px"><h4>Company</h4><ul><li>About Us</li><li>Awards</li><li>Careers</li><li>Customers</li><li>Events</li><li>Leadership</li><li>Partners</li><li>Press Room</li></ul></div>
  <div class="footer-col" style="left:421px"><h4>Products</h4><ul><li>All Products</li><li>People Counting &amp; Conversion</li><li>Queue Analytics</li><li>Staffing Optimization</li><li>Shopper Activity Maps</li><li>Display &amp; Window Effectiveness</li><li>Mobile In-store Analytics</li><li>VisitBase</li></ul></div>
  <div class="footer-col" style="left:664px"><h4>Resources</h4><ul><li>Downloads</li><li>Benchmark Report</li><li>Webinars</li><li>Blog</li></ul></div>
  <div class="footer-col social" style="left:871px"><h4>Follow us on</h4><ul><li><span class="icon"></span>Chirpline</li><li><span class="icon"></span>WorkNet</li><li><span class="icon"></span>FriendHub</li><li><span class="icon"></span>CircleUp</li></ul></div>
</footer>
<div class="copyright">Copyrights © 2015 Pain Relief Center</div>
</body>
</html>
```